Everything fresh, everything new

When I take over the practice, I would like to breathe new life into the practice. I want a business card design that catches the eye and brings a breath of fresh air

```html
<!DOCTYPE html>
<html lang="en">
<head>
<meta charset="utf-8">
<title>Praxisfeld – Business Card</title>
<link rel="stylesheet" href="https://fonts.googleapis.com/css2?family=Montserrat:wght@400;500;600;800&display=swap">
<style>
  :root {
    --stage: #141414;
    --card-dark: #464646;
    --card-light: #6a6a6a;
    --ink: #ffffff;
    --ink-soft: #ececec;
    --accent: #8cc63f;
  }
  * { box-sizing: border-box; margin: 0; padding: 0; }
  html, body {
    width: 1200px; height: 900px; overflow: hidden;
    background: radial-gradient(ellipse at 80% 10%, #333 0%, var(--stage) 60%);
    font-family: "Montserrat", sans-serif;
  }
  .stage {
    width: 1200px; height: 900px;
    display: flex; flex-direction: column; align-items: center; justify-content: center;
    gap: 44px;
  }
  .card {
    width: 630px; height: 360px; position: relative;
    background: linear-gradient(200deg, var(--card-light) 0%, var(--card-dark) 65%);
    box-shadow: 0 14px 30px rgba(0,0,0,.55);
    color: var(--ink);
  }
  .brand {
    display: flex; align-items: center; gap: 14px;
  }
  .brand-ring {
    border: 4px solid var(--accent); border-radius: 50%;
    flex: none;
  }
  .brand-name {
    font-weight: 600; color: var(--ink); letter-spacing: .5px;
  }
  .card-front { display: flex; align-items: center; justify-content: center; }
  .card-front .brand-ring { width: 54px; height: 54px; }
  .card-front .brand-name { font-size: 50px; }

  .card-back { display: flex; align-items: center; padding: 0 40px 0 42px; }
  .card-back .brand { width: 230px; }
  .card-back .brand-ring { width: 32px; height: 32px; border-width: 3px; }
  .card-back .brand-name { font-size: 29px; }
  .divider {
    width: 2px; height: 190px; background: var(--accent); margin: 0 30px 0 22px;
  }
  .contact { display: flex; flex-direction: column; }
  .person-name {
    font-weight: 800; font-size: 27px; color: var(--accent); letter-spacing: 2px; line-height: 1;
  }
  .person-role {
    font-size: 13px; font-weight: 500; letter-spacing: 1.5px; color: var(--ink-soft); margin-top: 4px;
  }
  .address {
    font-style: normal; font-size: 14px; line-height: 1.35; margin-top: 20px; color: var(--ink-soft);
  }
  .channels { list-style: none; margin-top: 18px; font-size: 14px; color: var(--ink-soft); }
  .channels li { display: flex; align-items: center; gap: 10px; margin-top: 6px; }
  .channels svg { width: 14px; height: 14px; flex: none; fill: var(--accent); }
</style>
</head>
<body>
<main class="stage">
  <section class="card card-front">
    <div class="brand">
      <span class="brand-ring"></span>
      <span class="brand-name">Praxisfeld</span>
    </div>
  </section>

  <section class="card card-back">
    <div class="brand">
      <span class="brand-ring"></span>
      <span class="brand-name">Praxisfeld</span>
    </div>
    <span class="divider"></span>
    <div class="contact">
      <h1 class="person-name">JONAS KELLER</h1>
      <p class="person-role">MANAGER</p>
      <address class="address">42 Linden Avenue 18<br>Your Country, MN 55120</address>
      <ul class="channels">
        <li>
          <svg viewBox="0 0 24 24" aria-hidden="true"><path d="M6.6 10.8a15.1 15.1 0 0 0 6.6 6.6l2.2-2.2a1 1 0 0 1 1-.25 11.4 11.4 0 0 0 3.6.57 1 1 0 0 1 1 1V20a1 1 0 0 1-1 1A17 17 0 0 1 3 4a1 1 0 0 1 1-1h3.5a1 1 0 0 1 1 1c0 1.25.2 2.45.57 3.57a1 1 0 0 1-.25 1z"/></svg>
          (555)014-2298
        </li>
        <li>
          <svg viewBox="0 0 24 24" aria-hidden="true"><path d="M2 5h20v2l-10 6L2 7zm0 4l10 6 10-6v10H2z"/></svg>
          info@youremail.com
        </li>
        <li>
          <svg viewBox="0 0 24 24" aria-hidden="true"><path d="M12 2a10 10 0 1 0 0 20 10 10 0 0 0 0-20zm0 2c.9 0 2.2 1.9 2.7 5H9.3C9.8 5.9 11.1 4 12 4zM4.3 11h3a18 18 0 0 0 0 2h-3a8 8 0 0 1 0-2zm5 0h5.4a16 16 0 0 1 0 2H9.3a16 16 0 0 1 0-2zm7.4 0h3a8 8 0 0 1 0 2h-3a18 18 0 0 0 0-2zM9.3 15h5.4c-.5 3.1-1.8 5-2.7 5s-2.2-1.9-2.7-5z"/></svg>
          www.yourwebsite.com
        </li>
      </ul>
    </div>
  </section>
</main>
</body>
</html>
```